Luxury 8’x4’ Acreage FOR SALE sign

I need (in 3 days) an outstanding Luxury - looking For Sale sign with my logo prominent & my brokerage logo to make up 9% of the total design space. It also needs to have “space” around it to breathe (as per brokerage qualification boundaries) It needs to be unique , have my phone number , my logo (with or without Real Estate cropped out) , brokerage logo & “for sale” or “available” or some type of wording that projects it’s a sign listing an acreage. My main focus is branding - MY logo & brand being recognized. I am unsure about including a photo of myself or not as I need this to look sleek & not busy! I have included a photo of the sign I designed & it’s just not doing it for me … I DO NOT want it to look like a business card. I’m finding it hard to make it look intentional with the DVK logo needed. It can be either logo - the box logo or the horizontal DVK logo but MUST make up 9%.
Updates

No photo of me please ! Decision made!

Target Market(s)

Luxury

Industry/Entity Type

Real Estate

Requirements
Must have
• Phone number, My logo, My Brokerage logo
Nice to have
• Needs to stand out “for sale” or “available” or

```html
<!DOCTYPE html>
<html lang="en">
<head>
<meta charset="utf-8">
<title>Jonas Zelmar – For Sale Sign</title>
<link href="https://fonts.googleapis.com/css2?family=Cinzel:wght@500;600&display=swap" rel="stylesheet">
<style>
  :root {
    --backdrop: #d4d4d4;
    --sign-black: #000000;
    --ink-white: #ffffff;
    --ink-black: #0a0a0a;
    --gold-light: #f5e28c;
    --gold-mid: #e2b960;
    --gold-deep: #d59e4e;
    --gold-line: #c9a04a;
  }
  html, body {
    margin: 0;
    padding: 0;
    width: 1200px;
    height: 1172px;
    overflow: hidden;
    background: var(--backdrop);
  }
  .sign {
    position: absolute;
    left: 60px;
    top: 316px;
    width: 1080px;
    height: 540px;
    background: var(--sign-black);
    font-family: "Cinzel", "Times New Roman", serif;
    color: var(--ink-white);
  }
  .agent-name {
    position: absolute;
    left: 100px;
    top: 52px;
    margin: 0;
    font-weight: 600;
    line-height: 1;
    letter-spacing: 1px;
  }
  .agent-name .first {
    display: block;
    font-size: 74px;
    margin-left: 118px;
  }
  .agent-name .last {
    display: block;
    font-size: 96px;
    margin-top: 8px;
  }
  .brokerage {
    position: absolute;
    left: 740px;
    top: 70px;
    width: 240px;
    text-align: center;
    font-weight: 600;
    line-height: 1;
  }
  .brokerage .mark {
    display: block;
    font-size: 82px;
    letter-spacing: 2px;
  }
  .brokerage .word {
    display: block;
    font-size: 34px;
    margin-top: 14px;
    letter-spacing: 1px;
  }
  .phone-band {
    position: absolute;
    left: 0;
    top: 260px;
    width: 100%;
    height: 142px;
    background: linear-gradient(90deg,
      var(--gold-light) 0%,
      var(--gold-mid) 18%,
      var(--gold-deep) 42%,
      var(--gold-light) 70%,
      var(--gold-mid) 88%,
      var(--gold-deep) 100%);
    display: flex;
    align-items: center;
    justify-content: center;
  }
  .phone {
    margin: 0;
    font-size: 128px;
    font-weight: 500;
    color: var(--ink-black);
    letter-spacing: 2px;
    line-height: 1;
  }
  .status {
    position: absolute;
    left: 116px;
    right: 116px;
    top: 420px;
    height: 100px;
    display: flex;
    align-items: center;
    gap: 16px;
  }
  .status .rule {
    flex: 1;
    height: 3px;
    background: linear-gradient(90deg, transparent 0%, var(--gold-line) 20%, var(--gold-light) 60%, var(--gold-line) 100%);
  }
  .status .rule.right {
    background: linear-gradient(90deg, var(--gold-line) 0%, var(--gold-light) 40%, var(--gold-line) 80%, transparent 100%);
  }
  .status .label {
    margin: 0;
    font-size: 74px;
    font-weight: 600;
    letter-spacing: 3px;
    line-height: 1;
  }
</style>
</head>
<body>
  <div class="sign">
    <h1 class="agent-name">
      <span class="first">JONAS</span>
      <span class="last">ZELMAR</span>
    </h1>

    <div class="brokerage">
      <span class="mark">DVK</span>
      <span class="word">REALTY</span>
    </div>

    <div class="phone-band">
      <p class="phone">403.555.0142</p>
    </div>

    <div class="status">
      <span class="rule left"></span>
      <p class="label">FOR SALE</p>
      <span class="rule right"></span>
    </div>
  </div>
</body>
</html>
```